New business card for civil engineering company - "Keystone Audit"

We need a business card designed for our new structural engineering company.

The company name is "Keystone Audit" logo files attached.

We would like the following:
* Two-sided card
* Simple design

Information to be placed on the card:
Name - Marcus Dellow
Job Title - Director / Structural Engineer
Credentials - BEng(Hons), CPEng, CMengNZ, IntPE(NZ)
Email - marcus.dellow@keystoneaudit.co.nz
mobile - 0219364058
website - www.keystoneaudit.co.nz

```html
<!DOCTYPE html>
<html lang="en">
<head>
<meta charset="utf-8">
<title>Keystone Audit – Business Card</title>
<link rel="stylesheet" href="https://fonts.googleapis.com/css2?family=Poppins:wght@400;600;700&display=swap">
<style>
  :root {
    --navy: #233c66;
    --navy-deep: #1f365d;
    --ink: #3a3a3a;
    --text: #2b2b2b;
    --paper: #ffffff;
    --backdrop: #222222;
    --accent: #3f7fc4;
  }
  * { margin: 0; padding: 0; box-sizing: border-box; }
  html, body {
    width: 1137px;
    height: 1200px;
    overflow: hidden;
    background: var(--backdrop);
    font-family: "Poppins", sans-serif;
  }
  .sheet {
    width: 1137px;
    height: 1200px;
    display: flex;
    flex-direction: column;
    align-items: center;
    justify-content: center;
    gap: 40px;
  }
  .card {
    width: 940px;
    height: 538px;
    position: relative;
    overflow: hidden;
  }

  /* Front */
  .card--front {
    background: var(--navy);
    display: flex;
    flex-direction: column;
    align-items: center;
    justify-content: center;
  }
  .brand {
    display: flex;
    flex-direction: column;
    align-items: center;
    color: var(--paper);
  }
  .brand__mark {
    display: flex;
    align-items: center;
    gap: 14px;
  }
  .brand__square {
    width: 22px;
    height: 22px;
    background: var(--accent);
  }
  .brand__name {
    font-weight: 600;
    font-size: 40px;
    letter-spacing: 4px;
    text-transform: uppercase;
  }
  .brand__tagline {
    margin-top: 10px;
    font-weight: 400;
    font-size: 15px;
    letter-spacing: 4.5px;
    text-transform: uppercase;
  }

  /* Back */
  .card--back {
    background: var(--paper);
    display: flex;
  }
  .card__panel {
    width: 263px;
    height: 100%;
    background: var(--navy);
    display: flex;
    align-items: center;
    justify-content: center;
  }
  .card__panel .brand__name { font-size: 17px; letter-spacing: 2px; }
  .card__panel .brand__square { width: 11px; height: 11px; }
  .card__panel .brand__mark { gap: 8px; }
  .card__panel .brand__tagline { font-size: 8px; letter-spacing: 2.2px; margin-top: 5px; }

  .contact {
    padding: 112px 0 0 107px;
  }
  .contact__name {
    color: var(--navy);
    font-weight: 700;
    font-size: 38px;
    line-height: 1.1;
  }
  .contact__role {
    color: var(--ink);
    font-weight: 600;
    font-size: 22px;
    margin-top: 4px;
  }
  .contact__list {
    list-style: none;
    margin-top: 56px;
  }
  .contact__item {
    display: flex;
    align-items: center;
    color: var(--text);
    font-size: 22px;
    height: 41px;
  }
  .contact__icon {
    width: 22px;
    height: 22px;
    margin-right: 20px;
    fill: var(--navy);
    flex: none;
  }
</style>
</head>
<body>
<main class="sheet">

  <section class="card card--front" aria-label="Card front">
    <div class="brand">
      <div class="brand__mark">
        <span class="brand__square"></span>
        <span class="brand__name">Keystone Audit</span>
      </div>
      <span class="brand__tagline">Peer Review Specialists</span>
    </div>
  </section>

  <section class="card card--back" aria-label="Card back">
    <div class="card__panel">
      <div class="brand">
        <div class="brand__mark">
          <span class="brand__square"></span>
          <span class="brand__name">Keystone Audit</span>
        </div>
        <span class="brand__tagline">Peer Review Specialists</span>
      </div>
    </div>

    <div class="contact">
      <h1 class="contact__name">Marcus Dellow</h1>
      <p class="contact__role">Director / Structural Engineer</p>
      <ul class="contact__list">
        <li class="contact__item">
          <svg class="contact__icon" viewBox="0 0 24 24" aria-hidden="true"><path d="M12 2a7 7 0 0 0-7 7c0 5 7 13 7 13s7-8 7-13a7 7 0 0 0-7-7zm0 9.5A2.5 2.5 0 1 1 12 6.5a2.5 2.5 0 0 1 0 5z"/></svg>
          BEng(Hons), CPEng, CMengNZ, IntPE(NZ)
        </li>
        <li class="contact__item">
          <svg class="contact__icon" viewBox="0 0 24 24" aria-hidden="true"><path d="M2 5h20v14H2z M3.5 6.5 12 13l8.5-6.5" fill="none" stroke="#233c66" stroke-width="0"/><path d="M2 5h20v14H2V5zm2 2v.3l8 5.7 8-5.7V7H4zm0 2.7V17h16V9.7l-8 5.6-8-5.6z"/></svg>
          marcus.dellow@keystoneaudit.co.nz
        </li>
        <li class="contact__item">
          <svg class="contact__icon" viewBox="0 0 24 24" aria-hidden="true"><path d="M6.6 10.8a15.1 15.1 0 0 0 6.6 6.6l2.2-2.2a1 1 0 0 1 1-.25 11.4 11.4 0 0 0 3.6.57 1 1 0 0 1 1 1V20a1 1 0 0 1-1 1A17 17 0 0 1 3 4a1 1 0 0 1 1-1h3.5a1 1 0 0 1 1 1c0 1.25.2 2.45.57 3.6a1 1 0 0 1-.25 1z"/></svg>
          021-936-4058
        </li>
        <li class="contact__item">
          <svg class="contact__icon" viewBox="0 0 24 24" aria-hidden="true"><path d="M12 2a10 10 0 1 0 0 20 10 10 0 0 0 0-20zm6.9 6h-3a15.6 15.6 0 0 0-1.4-3.6A8 8 0 0 1 18.9 8zM12 4c.8 1.2 1.5 2.5 1.9 4h-3.8c.4-1.5 1.1-2.8 1.9-4zM4.3 14a8 8 0 0 1 0-4h3.4a16 16 0 0 0 0 4H4.3zm.8 2h3a15.6 15.6 0 0 0 1.4 3.6A8 8 0 0 1 5.1 16zm3-8h-3a8 8 0 0 1 4.4-3.6A15.6 15.6 0 0 0 8.1 8zM12 20c-.8-1.2-1.5-2.5-1.9-4h3.8c-.4 1.5-1.1 2.8-1.9 4zm2.3-6H9.7a14.7 14.7 0 0 1 0-4h4.6a14.7 14.7 0 0 1 0 4zm.2 5.6a15.6 15.6 0 0 0 1.4-3.6h3a8 8 0 0 1-4.4 3.6zm1.8-5.6a16 16 0 0 0 0-4h3.4a8 8 0 0 1 0 4h-3.4z"/></svg>
          www.keystoneaudit.co.nz
        </li>
      </ul>
    </div>
  </section>

</main>
</body>
</html>
```